PTA Meeting Poster

We are looking to create a poster to invite parents of our school to our monthly PTA Meeting.

The copy should include:

PTA Meeting
This Wednesday
8:40am
in the Multi Purpose Room

All Welcome!

```html
<!DOCTYPE html>
<html lang="en">
<head>
<meta charset="utf-8">
<title>PTA Meeting Poster</title>
<link rel="stylesheet" href="https://fonts.googleapis.com/css2?family=Cinzel:wght@400;600&family=Pinyon+Script&display=swap">
<style>
  :root {
    --sky-pale: #99ffff;
    --sky: #00ccff;
    --aqua: #00ffff;
    --sun: #ffff00;
    --white: #ffffff;
  }
  * { margin: 0; padding: 0; box-sizing: border-box; }
  html, body { width: 899px; height: 1200px; overflow: hidden; background: var(--sky-pale); }
  .poster { position: relative; width: 899px; height: 1200px; background: var(--sky-pale); }
  .poster__frame {
    position: absolute; left: 57px; top: 57px; width: 787px; height: 1086px;
    border: 7px solid var(--white); background: var(--sky);
  }
  .title {
    position: absolute; left: 0; width: 899px; text-align: center;
    font-family: "Cinzel", serif; font-weight: 600; color: var(--sun);
    text-shadow: 5px 4px 0 var(--aqua); line-height: 1;
  }
  .title--pta { top: 100px; font-size: 152px; }
  .title--meeting { top: 245px; font-size: 160px; letter-spacing: -2px; }
  .info-box {
    position: absolute; left: 135px; width: 638px; height: 146px;
    border: 4px solid var(--sun);
    display: flex; flex-direction: column; justify-content: center; align-items: center;
    font-family: "Cinzel", serif; color: var(--white); font-size: 54px; line-height: 64px;
  }
  .info-box__shadow { position: absolute; left: 217px; width: 556px; height: 8px; background: var(--aqua); }
  .info-box--when { top: 503px; }
  .shadow--when { top: 649px; }
  .info-box--where { top: 705px; }
  .shadow--where { top: 850px; }
  .welcome {
    position: absolute; left: 0; top: 975px; width: 899px; text-align: center;
    font-family: "Pinyon Script", cursive; color: var(--white); font-size: 118px; line-height: 1;
  }
</style>
</head>
<body>
  <main class="poster">
    <div class="poster__frame"></div>
    <h1>
      <span class="title title--pta">PTA</span>
      <span class="title title--meeting">Meeting</span>
    </h1>
    <div class="info-box__shadow shadow--when"></div>
    <p class="info-box info-box--when"><span>This Wednesday</span><span>8:40am</span></p>
    <div class="info-box__shadow shadow--where"></div>
    <p class="info-box info-box--where"><span>in the</span><span>Multi Purpose Room</span></p>
    <p class="welcome">All Welcome!</p>
  </main>
</body>
</html>
```